Design for a very long wall that will be wall printed. The name of the facility is "Brisk Gallery"

The space I am working on has a 30' x 8' wall. It is a wall that is located in a under construction Design Showroom where contractors of all trades can have an office and put out their banners and different items for customers to come and see. so there could be roofers, construction, cabinet installers and designers, gutters and other trades can rent an office in the space and bring their customers and sit down and talk about what they need. I want the design for the wall to have a bold punch and it will be printed on the wall with a high definition wall printer. The walls are arctic white right now and I can send the color codes for the color the wall is currently. The wall printer has the capability to do white as well. I am including some pics of the space and an example wall print.

Target Market(s)

Contractors and Customers of Contractors

Industry/Entity Type

all trades. Photos are to demonstrate the capabilities of the printer that will be used

Requirements
Must have
• Perhaps have a person or persons int he design, a human element and perhaps some abstract elements as well
Nice to have
• Perhaps some architecture or perhaps an interior cabinet or fixtures. Glass doors and or walls. Perhaps incorporate the name "Brisk Gallery"

```html
<!DOCTYPE html>
<html lang="en">
<head>
<meta charset="utf-8">
<title>Brisk Gallery – Wall Print</title>
<link href="https://fonts.googleapis.com/css2?family=Montserrat:wght@600&display=swap" rel="stylesheet">
<style>
  :root {
    --canvas: #333333;
    --paper: #ffffff;
    --brand-yellow: #ffcd00;
    --cross-grey: #808080;
    --accent-navy: #10182b;
    --title-edge: #8a8a8a;
    --photo-light: #f1ede8;
    --photo-warm: #d99a3a;
  }
  * { margin: 0; padding: 0; box-sizing: border-box; }
  html, body { width: 1200px; height: 1200px; overflow: hidden; background: var(--canvas); }
  .stage { position: relative; width: 1200px; height: 1200px; background: var(--canvas); }
  .wall-banner {
    position: absolute;
    left: 68.8px; top: 462.4px;
    width: 1062.4px; height: 283.2px;
    background: var(--paper);
    overflow: hidden;
  }
  .wall-banner svg.shapes { position: absolute; inset: 0; width: 100%; height: 100%; }
  .shape-yellow { fill: var(--brand-yellow); }
  .shape-navy { fill: var(--accent-navy); }
  .cross { stroke: var(--cross-grey); stroke-width: 5; stroke-linecap: butt; }
  .worker-photo {
    position: absolute;
    left: 340.8px; top: 5.6px;
    width: 206.4px; height: 277.6px;
    background: linear-gradient(180deg, var(--photo-light) 0%, var(--photo-light) 55%, var(--photo-warm) 100%);
    border-radius: 90px 90px 0 0;
  }
  .facility-name {
    position: absolute;
    right: 6px; top: 176px;
    font-family: "Montserrat", sans-serif;
    font-weight: 600;
    font-size: 48px;
    line-height: 1;
    letter-spacing: -0.5px;
    color: var(--brand-yellow);
    -webkit-text-stroke: 0.8px var(--title-edge);
    white-space: nowrap;
  }
</style>
</head>
<body>
<div class="stage">
  <section class="wall-banner">
    <svg class="shapes" viewBox="0 0 1062.4 283.2" aria-hidden="true">
      <!-- frame bars -->
      <rect class="shape-yellow" x="0" y="0" width="176.8" height="38.4"/>
      <rect class="shape-yellow" x="0" y="0" width="38.4" height="283.2"/>
      <rect class="shape-yellow" x="0" y="244.8" width="555.2" height="38.4"/>
      <rect class="shape-yellow" x="672" y="230.4" width="390.4" height="52.8"/>
      <!-- cross row -->
      <g class="cross">
        <path d="M212 12 l24 24 M236 12 l-24 24"/>
        <path d="M268 12 l24 24 M292 12 l-24 24"/>
        <path d="M324 12 l24 24 M348 12 l-24 24"/>
        <path d="M380 12 l24 24 M404 12 l-24 24"/>
      </g>
      <!-- navy squares -->
      <g class="shape-navy">
        <rect x="346" y="234.4" width="10.4" height="10.4"/>
        <rect x="390" y="234.4" width="10.4" height="10.4"/>
        <rect x="390" y="258.4" width="10.4" height="10.4"/>
        <rect x="526" y="234.4" width="10.4" height="10.4"/>
        <rect x="570" y="234.4" width="10.4" height="10.4"/>
        <rect x="570" y="258.4" width="10.4" height="10.4"/>
        <rect x="614" y="258.4" width="10.4" height="10.4"/>
      </g>
      <!-- dot triangle -->
      <g class="shape-yellow">
        <rect x="903.2" y="20" width="4.8" height="4.8"/>
        <rect x="927.2" y="20" width="4.8" height="4.8"/><rect x="927.2" y="34.4" width="4.8" height="4.8"/>
        <rect x="951.2" y="20" width="4.8" height="4.8"/><rect x="951.2" y="34.4" width="4.8" height="4.8"/><rect x="951.2" y="48.8" width="4.8" height="4.8"/>
        <rect x="975.2" y="20" width="4.8" height="4.8"/><rect x="975.2" y="34.4" width="4.8" height="4.8"/><rect x="975.2" y="48.8" width="4.8" height="4.8"/><rect x="975.2" y="63.2" width="4.8" height="4.8"/>
        <rect x="999.2" y="20" width="4.8" height="4.8"/><rect x="999.2" y="34.4" width="4.8" height="4.8"/><rect x="999.2" y="48.8" width="4.8" height="4.8"/><rect x="999.2" y="63.2" width="4.8" height="4.8"/><rect x="999.2" y="77.6" width="4.8" height="4.8"/>
        <rect x="1023.2" y="20" width="4.8" height="4.8"/><rect x="1023.2" y="34.4" width="4.8" height="4.8"/><rect x="1023.2" y="48.8" width="4.8" height="4.8"/><rect x="1023.2" y="63.2" width="4.8" height="4.8"/><rect x="1023.2" y="77.6" width="4.8" height="4.8"/><rect x="1023.2" y="92" width="4.8" height="4.8"/>
      </g>
    </svg>
    <div class="worker-photo" role="img" aria-label="Photo of a cheerful tradeswoman in a white T-shirt, work gloves and a tool belt, making a call-me gesture"></div>
    <h1 class="facility-name">Brisk Gallery</h1>
  </section>
</div>
</body>
</html>
```